Party flyer design

Hi ArtHive,

I need a party flyer designed incorporating my logo and the verbiage stated below for a
social get-together I'm throwing at a local martini bar and lounge in my local area.

I've attached my logo and a copy of a flyer I've seen that incorporates the look and feel I'm looking for.

Thanks

Lumora 4 presents
Velvet Hour Mixers

Join us Fridays at 11:00 PM - 2:00 AM
at At The Quill Westbrook
27315 Harlow Ridge, Suite 340
Charlotte, NC 28193

For more details email us at info@lumora4.com

```html
<!DOCTYPE html>
<html lang="en">
<head>
<meta charset="utf-8">
<title>Velvet Hour Mixers – Flyer</title>
<link rel="stylesheet" href="https://fonts.googleapis.com/css2?family=Anton&family=Bebas+Neue&family=Great+Vibes&family=Open+Sans:wght@700&family=Arimo:wght@700&display=swap">
<style>
  :root {
    --page-bg: #e6e4e8;
    --paper: #ffffff;
    --blush: #f6dde4;
    --ice-light: #eef5fb;
    --ice-mid: #b9d7ee;
    --ice-deep: #5f9fd2;
    --title-top: #d6e6fb;
    --title-bottom: #6e93d8;
    --title-edge: #27407a;
    --script: #7a2fb2;
    --bar-dark: #4d1880;
    --bar-bright: #7d2fd6;
    --bar-address: #6a22b8;
    --ink: #111111;
    --logo-orange: #e8501c;
    --white: #ffffff;
  }
  * { margin: 0; padding: 0; box-sizing: border-box; }
  html, body {
    width: 900px; height: 1200px; overflow: hidden;
    background: var(--page-bg);
  }
  .flyer {
    position: absolute; left: 80px; top: 54px;
    width: 740px; height: 1092px;
    background: var(--paper);
    overflow: hidden;
    box-shadow: 0 6px 24px rgba(0,0,0,.18);
  }
  .flyer__blush-disc {
    position: absolute; right: -120px; top: -60px;
    width: 520px; height: 520px; border-radius: 50%;
    background: var(--blush); opacity: .55;
  }
  .flyer__blush-band {
    position: absolute; left: 0; right: 0; top: 850px; height: 242px;
    background: var(--blush); opacity: .5;
  }
  .art-splash {
    position: absolute; left: 0; top: 60px; width: 740px; height: 830px;
    background: radial-gradient(ellipse 55% 48% at 50% 48%, var(--ice-mid) 0%, var(--ice-light) 55%, rgba(255,255,255,0) 80%);
  }
  .art-drinks {
    position: absolute; left: 90px; top: 70px; width: 580px; height: 300px;
    background: radial-gradient(ellipse 50% 50% at 50% 55%, rgba(95,159,210,.45), rgba(185,215,238,.15) 70%, rgba(255,255,255,0));
  }
  .art-ice {
    position: absolute; left: 0; bottom: 0; width: 740px; height: 210px;
    background: linear-gradient(180deg, rgba(185,215,238,0) 0%, var(--ice-mid) 45%, var(--ice-light) 100%);
  }
  .brand {
    position: absolute; left: 38px; top: 50px;
    display: flex; flex-direction: column; align-items: flex-start;
  }
  .brand__mark {
    width: 52px; height: 52px; border-radius: 50%;
    background: var(--logo-orange); margin-left: 40px;
  }
  .brand__name {
    font-family: "Open Sans", sans-serif; font-weight: 700;
    font-size: 28px; color: var(--logo-orange); margin-top: 4px;
  }
  .brand__presents {
    font-family: "Open Sans", sans-serif; font-weight: 700;
    font-size: 27px; color: var(--ink); margin-top: 2px;
  }
  .title {
    position: absolute; left: 0; top: 350px; width: 740px; height: 340px;
  }
  .title__block {
    font-family: "Anton", sans-serif; font-size: 150px;
    fill: url(#titleFill); stroke: var(--title-edge); stroke-width: 3px;
    paint-order: stroke;
  }
  .title__script {
    font-family: "Great Vibes", cursive; font-size: 112px;
    fill: var(--script); stroke: var(--white); stroke-width: 6px;
    paint-order: stroke;
  }
  .info-bar {
    position: absolute; color: var(--white); text-align: center;
    display: flex; align-items: center; justify-content: center;
    white-space: nowrap; line-height: 1;
  }
  .info-bar--time {
    left: 108px; top: 703px; width: 500px; height: 70px;
    background: var(--bar-dark);
    font-family: "Bebas Neue", sans-serif; font-size: 46px;
    padding-top: 4px;
  }
  .info-bar--venue {
    left: 124px; top: 779px; width: 494px; height: 70px;
    background: var(--bar-bright);
    font-family: "Bebas Neue", sans-serif; font-size: 50px;
    padding-top: 4px;
  }
  .info-bar--address {
    left: 114px; top: 851px; width: 488px; height: 82px;
    background: var(--bar-address);
    font-family: "Arimo", sans-serif; font-weight: 700;
    font-size: 25px; line-height: 1.3; flex-direction: column;
  }
  .contact {
    position: absolute; left: 0; right: 0; bottom: 14px;
    text-align: center; white-space: nowrap;
    font-family: "Open Sans", sans-serif; font-weight: 700;
    font-size: 23px; color: var(--ink);
  }
</style>
</head>
<body>
  <main class="flyer">
    <div class="flyer__blush-disc"></div>
    <div class="flyer__blush-band"></div>

    <div class="art-splash" role="img" aria-label="Splashing water around the title"></div>
    <div class="art-drinks" role="img" aria-label="Bottle, martini glass with olives and whisky glass among ice cubes"></div>
    <div class="art-ice" role="img" aria-label="Pile of ice cubes"></div>

    <header class="brand">
      <span class="brand__mark"></span>
      <span class="brand__name">Lumora 4</span>
      <span class="brand__presents">Presents..</span>
    </header>

    <svg class="title" viewBox="0 0 740 340" aria-label="Velvet Hour Mixers">
      <defs>
        <linearGradient id="titleFill" x1="0" y1="0" x2="0" y2="1">
          <stop offset="0" stop-color="var(--title-top)"/>
          <stop offset="1" stop-color="var(--title-bottom)"/>
        </linearGradient>
      </defs>
      <text class="title__block" x="124" y="140" textLength="497" lengthAdjust="spacingAndGlyphs">VELVET</text>
      <text class="title__block" x="124" y="272" textLength="470" lengthAdjust="spacingAndGlyphs">HOUR</text>
      <text class="title__script" x="220" y="305" textLength="380" lengthAdjust="spacingAndGlyphs">Mixers</text>
    </svg>

    <div class="info-bar info-bar--time">FRIDAYS&nbsp; 11:00 PM - 2:00 AM</div>
    <div class="info-bar info-bar--venue">AT THE QUILL WESTBROOK</div>
    <div class="info-bar info-bar--address">
      <span>27315 Harlow Ridge, Suite 340</span>
      <span>Charlotte, NC 28193</span>
    </div>

    <p class="contact">For more details email us at info@lumora4.com</p>
  </main>
</body>
</html>
```